Bref créative
Norland Equity Partners
Investing
Professional
Tom Radcliffe
President
728 Maplewood Ave. Suite 310
Oak Terrace, CA 90418
tom@NorlandEquityPartners.com
www.NorlandEquityPartners.com
We want our logo to be the main component of the card. Have fun and let me see what you got!
Feel free to try 1 or 2 sided card ideas.
Can use other fonts besides the logo font if you desire.

```html
<!DOCTYPE html>
<html lang="en">
<head>
<meta charset="utf-8">
<title>Norland Equity Partners – Business Cards</title>
<link href="https://fonts.googleapis.com/css2?family=Roboto:wght@300;400;500&display=swap" rel="stylesheet">
<style>
  :root {
    --brand-red: #e4262b;
    --ink: #222222;
    --muted: #555555;
    --card-white: #ffffff;
    --canvas: #e9e9e7;
    --rule: #333333;
  }
  * { box-sizing: border-box; margin: 0; padding: 0; }
  html, body { width: 1200px; height: 761px; overflow: hidden; }
  body {
    background: var(--canvas);
    font-family: "Roboto", Arial, sans-serif;
    color: var(--ink);
    position: relative;
  }
  .card {
    position: absolute;
    width: 475px;
    height: 272px;
    border-radius: 24px;
    background: var(--card-white);
    box-shadow: 0 2px 6px rgba(0,0,0,0.12);
  }
  .card--info  { left: 391px; top: 17px; }
  .card--red   { left: 144px; top: 440px; background: var(--brand-red); }
  .card--plain { left: 653px; top: 440px; }

  .wordmark {
    position: absolute;
    left: 0; right: 0;
    display: flex;
    flex-direction: column;
    align-items: center;
  }
  .wordmark__row { display: flex; align-items: center; gap: 14px; }
  .wordmark__dot {
    width: 44px; height: 44px; border-radius: 50%;
    background: var(--brand-red);
  }
  .wordmark__name {
    font-weight: 300;
    font-size: 24px;
    letter-spacing: 3px;
    text-transform: uppercase;
    color: var(--ink);
  }
  .wordmark__rule {
    width: 300px; height: 1px; background: var(--rule); margin-top: 10px;
  }
  .card--info .wordmark { top: 34px; }
  .card--red .wordmark, .card--plain .wordmark { top: 92px; }
  .card--red .wordmark__dot { background: var(--card-white); }
  .card--red .wordmark__name { color: var(--card-white); }
  .card--red .wordmark__rule { background: var(--card-white); }

  .contact-list {
    position: absolute; left: 34px; top: 148px;
    list-style: none; font-size: 11px; color: var(--muted); line-height: 1.35;
  }
  .contact-list li { display: flex; align-items: flex-start; gap: 8px; margin-bottom: 3px; }
  .contact-list svg { flex: none; width: 12px; height: 12px; margin-top: 1px; }
  .contact-list .address { display: block; }

  .person { position: absolute; right: 34px; top: 160px; text-align: left; }
  .person__name { color: var(--brand-red); font-size: 18px; font-weight: 400; }
  .person__title { font-size: 12px; color: var(--ink); margin-top: 2px; }

  .card__url {
    position: absolute; left: 0; right: 0; bottom: 22px;
    text-align: center; font-size: 10px; color: var(--brand-red);
  }
  .card--red .card__url { color: var(--card-white); }
</style>
</head>
<body>

<section class="card card--info" aria-label="Business card front with contact details">
  <div class="wordmark">
    <div class="wordmark__row">
      <span class="wordmark__dot"></span>
      <span class="wordmark__name">Norland Equity Partners</span>
    </div>
    <span class="wordmark__rule"></span>
  </div>

  <ul class="contact-list">
    <li>
      <svg viewBox="0 0 12 12" aria-hidden="true"><circle cx="6" cy="6" r="6" fill="var(--brand-red)"/><path d="M6 2.6a2 2 0 0 0-2 2c0 1.6 2 4 2 4s2-2.4 2-4a2 2 0 0 0-2-2z" fill="#fff"/></svg>
      <span class="address">728 Maplewood Ave. Suite 310<br>Oak Terrace, CA 90418</span>
    </li>
    <li>
      <svg viewBox="0 0 12 12" aria-hidden="true"><circle cx="6" cy="6" r="6" fill="var(--brand-red)"/><path d="M4 3h1.2l.6 1.5-.8.6a4 4 0 0 0 1.9 1.9l.6-.8L9 6.8V8a1 1 0 0 1-1 1A5 5 0 0 1 3 4a1 1 0 0 1 1-1z" fill="#fff"/></svg>
      <span>310-555-0142</span>
    </li>
    <li>
      <svg viewBox="0 0 12 12" aria-hidden="true"><circle cx="6" cy="6" r="6" fill="var(--brand-red)"/><rect x="3" y="4" width="6" height="4.2" fill="#fff"/><path d="M3 4l3 2.4L9 4" fill="none" stroke="var(--brand-red)" stroke-width=".7"/></svg>
      <span>tom@NorlandEquityPartners.com</span>
    </li>
    <li>
      <svg viewBox="0 0 12 12" aria-hidden="true"><circle cx="6" cy="6" r="6" fill="var(--brand-red)"/><circle cx="6" cy="6" r="3" fill="none" stroke="#fff" stroke-width=".8"/><path d="M3 6h6M6 3v6" stroke="#fff" stroke-width=".6"/></svg>
      <span>www.NorlandEquityPartners.com</span>
    </li>
  </ul>

  <div class="person">
    <p class="person__name">Tom Radcliffe</p>
    <p class="person__title">President</p>
  </div>
</section>

<section class="card card--red" aria-label="Business card back, red">
  <div class="wordmark">
    <div class="wordmark__row">
      <span class="wordmark__dot"></span>
      <span class="wordmark__name">Norland Equity Partners</span>
    </div>
    <span class="wordmark__rule"></span>
  </div>
  <p class="card__url">www.NorlandEquityPartners.com</p>
</section>

<section class="card card--plain" aria-label="Business card back, white">
  <div class="wordmark">
    <div class="wordmark__row">
      <span class="wordmark__dot"></span>
      <span class="wordmark__name">Norland Equity Partners</span>
    </div>
    <span class="wordmark__rule"></span>
  </div>
  <p class="card__url">www.NorlandEquityPartners.com</p>
</section>

</body>
</html>
```